Varn Medical needs bold attention catching website for healthcare professionals(target)

I need a hero page as well as a products and about page for a website of mine. I specialize in orthopedic instruments . Specifically bone drills and saws. This whole company was founded to bring superb quality highly discounted medical instruments. Specifically bone drills, bone saws, k-wires and pins. Two main points should be cost savings and superior quality.

Target Market(s)

healthcare professionals Surgeons and hospital material managers

Number of Pages Required

3 page

Font styles to use
Serif

Colors

Designer to choose colors to be used in the design.

Requirements
Must have
• colors should match logo design

```html
<!DOCTYPE html>
<html lang="en">
<head>
<meta charset="utf-8">
<title>Varn Medical – Website Design</title>
<link href="https://fonts.googleapis.com/css2?family=Oswald:wght@500;600&family=Roboto:wght@300;400;500&display=swap" rel="stylesheet">
<style>
  :root{
    --blue:#2f97f3;
    --blue-soft:#5aaef5;
    --ink:#3c3c3c;
    --muted:#666;
    --line:#e7e7e7;
    --paper:#ffffff;
    --mist:#f3f5f7;
    --footer:#6e6e6e;
    --steel-a:#f4f6f8;
    --steel-b:#a9b1ba;
  }
  *{margin:0;padding:0;box-sizing:border-box}
  html,body{width:1200px;height:1200px;overflow:hidden;background:var(--paper)}
  body{position:relative;font-family:'Roboto',sans-serif;color:var(--ink)}

  .page{position:absolute;top:0;width:599px;background:var(--paper);overflow:hidden}
  .page--thumb{left:150px;height:2348px;transform:scale(.5109);transform-origin:0 0}
  .page--full{left:525px;height:1200px}

  .abs{position:absolute}

  /* navigation */
  .nav-logo{left:87px;top:15px;font-size:14px;font-weight:400;color:#555;letter-spacing:.2px;font-family:'Roboto',sans-serif}
  .nav-links{top:20px;left:340px;display:flex;gap:13px;font-size:6.6px;font-weight:500;color:#333;letter-spacing:.2px}
  .nav-links span{padding:1px 2px}
  .nav-links .is-active{color:var(--blue);border:1px solid var(--blue)}

  /* hero */
  .hero{left:0;top:46px;width:599px;height:492px}
  .hero-kicker{left:348px;top:280px;font-family:'Oswald',sans-serif;font-weight:500;font-size:20px;color:#fff;letter-spacing:.1px}
  .hero-title{left:347px;top:306px;font-family:'Oswald',sans-serif;font-weight:600;font-size:35px;line-height:1.02;color:#fff;letter-spacing:.3px}
  .btn{display:flex;align-items:center;justify-content:center;font-family:'Oswald',sans-serif;font-weight:500;border:2px solid;background:transparent}
  .hero-btn{left:347px;top:398px;width:119px;height:32px;font-size:15px;color:#fff;border-color:#fff}

  /* about */
  .about{left:0;top:601px;width:599px;height:343px}
  .about-title{left:297px;top:22px;font-size:22px;font-weight:400;color:#fff;letter-spacing:.3px}
  .about-copy{left:293px;top:104px;width:225px;font-size:9.5px;line-height:12.2px;color:#555}
  .about-copy p+p{margin-top:12px}
  .about-btn{left:294px;top:254px;width:119px;height:31px;font-size:15px;color:var(--blue);border-color:var(--blue);background:#fff}

  /* section headings */
  .sec-title{left:0;width:599px;text-align:center;font-size:16px;color:var(--blue);letter-spacing:.2px}
  .sec-rule{left:211px;width:182px;height:1.5px;background:var(--blue)}
  .eyebrow{left:0;width:599px;text-align:center;font-size:8.6px;color:#555;letter-spacing:.2px}

  /* category cards */
  .cat{top:1077px;width:100px}
  .cat-thumb{height:100px;border:1.5px solid var(--blue);background:#fff;display:flex;align-items:center;justify-content:center}
  .cat-thumb i{display:block;width:56px;height:64px;border-radius:6px;background:linear-gradient(135deg,var(--steel-a),var(--steel-b))}
  .cat-label{margin-top:5px;height:35px;background:var(--blue);color:#fff;font-size:9.4px;text-align:center;display:flex;align-items:center;justify-content:center;text-transform:uppercase;line-height:1.15;padding:0 4px}

  /* product detail */
  .detail-title{left:109px;top:1243px;font-size:11px;color:#222;font-weight:500}
  .detail-title span{color:var(--blue);font-weight:400}
  .detail-rule{left:109px;top:1259px;width:50px;height:1px;background:var(--blue)}
  .detail-copy{left:109px;top:1270px;width:168px;font-size:5.6px;line-height:8px;color:#777}
  .detail-btn{left:109px;top:1352px;width:28px;height:10px;border:1px solid var(--blue)}
  .detail-hero{left:305px;top:1266px;width:184px;height:160px;border-radius:10px;background:linear-gradient(135deg,#f7f8fa,#aeb6be)}
  .detail-shadow{left:345px;top:1438px;width:100px;height:18px;border-radius:50%;background:#eee}
  .thumb{width:54px;height:48px;border-radius:4px;background:linear-gradient(135deg,var(--steel-a),var(--steel-b))}
  .thumb.is-selected{background:linear-gradient(135deg,#a9d2fa,var(--blue-soft))}
  .detail-arrow{left:313px;top:1436px;font-size:14px;color:var(--blue)}

  /* why choose */
  .why-band{left:0;top:1503px;width:599px;height:454px;background:var(--mist)}
  .why-panel{left:0;top:1558px;width:599px;height:372px;background:linear-gradient(160deg,#4aa6f5,#6fb8f5 55%,#4aa3f4)}
  .why-card{width:126px;height:82px;background:#fff;padding:20px 8px 0;text-align:center}
  .why-card b{display:block;font-size:6px;font-weight:500;color:var(--blue);margin-bottom:5px}
  .why-card p{font-size:4.6px;line-height:6.4px;color:#888}
  .why-icon{width:18px;height:18px;border-radius:50%;background:var(--blue);border:2px solid #fff;display:flex;align-items:center;justify-content:center}
  .why-icon i{width:6px;height:6px;border-radius:50%;border:1.5px solid #fff}
  .why-quote{left:0;top:1822px;width:599px;text-align:center;font-size:12.5px;line-height:24px;color:#fff;text-transform:uppercase}

  /* testimonials */
  .tst-side{top:2020px;height:110px;background:linear-gradient(135deg,#d6e9fb,#9fcdf6)}
  .tst-main{left:206px;top:2012px;width:199px;height:129px;background:#fff;box-shadow:0 0 6px rgba(0,0,0,.08)}
  .tst-photo{height:67px;background:linear-gradient(135deg,#b7dbfb,#75b8f3)}
  .tst-main b{display:block;text-align:center;font-size:6px;font-weight:500;color:var(--blue);margin:10px 0 4px}
  .tst-main p{padding:0 18px;text-align:center;font-size:4.6px;line-height:6.4px;color:#999}

  /* footer */
  .footer{left:0;top:2214px;width:599px;height:134px}
  .footer-logo{left:0;top:2228px;width:599px;text-align:center;font-size:16px;color:#fff;font-weight:400}
  .footer-line{left:190px;top:2252px;width:220px;text-align:center;font-size:4.6px;line-height:6.4px;color:#ddd}
  .footer-col{top:2280px;font-size:4.8px;line-height:7.5px;color:#ddd}
  .footer-input{left:320px;top:2292px;width:90px;height:14px;border:1px solid #ddd;background:#fff}
  .footer-input i{position:absolute;right:0;top:0;width:24px;height:12px;background:var(--blue)}
</style>
</head>
<body>

<!-- ============ Full layout, reduced ============ -->
<div class="page page--thumb">
  <div class="abs nav-logo">Varn Medical</div>
  <nav class="abs nav-links"><span>HOME</span><span class="is-active">ABOUT</span><span>PRODUCTS</span><span>BLOG</span><span>CONTACT</span></nav>

  <svg class="abs hero" viewBox="0 0 599 492">
    <defs>
      <clipPath id="heroClipA"><path d="M0 0H599V418C599 462 545 492 459 492H0Z"/></clipPath>
      <linearGradient id="heroPhotoA" x1="0" y1="0" x2="1" y2="1"><stop offset="0" stop-color="#f1f3f5"/><stop offset=".55" stop-color="#d9dfe5"/><stop offset="1" stop-color="#b9c6d6"/></linearGradient>
    </defs>
    <g clip-path="url(#heroClipA)">
      <rect width="599" height="418" fill="url(#heroPhotoA)" role="img" aria-label="Photo of a smiling doctor in a white coat talking with an older patient in a bright clinic"/>
      <rect y="418" width="599" height="74" fill="var(--blue)"/>
      <circle cx="501" cy="372" r="200" fill="var(--blue)"/>
    </g>
  </svg>
  <div class="abs hero-kicker">Hospitals and Physicians</div>
  <div class="abs hero-title">HIGH-QUALITY<br>PRODUCTS</div>
  <div class="abs btn hero-btn">Read More</div>

  <svg class="abs about" viewBox="0 0 599 343">
    <defs><linearGradient id="aboutBgA" x1="0" y1="0" x2="1" y2="1"><stop offset="0" stop-color="#fff"/><stop offset="1" stop-color="#eef2f5"/></linearGradient>
    <linearGradient id="aboutPhotoA" x1="0" y1="0" x2="0" y2="1"><stop offset="0" stop-color="#eef4fa"/><stop offset="1" stop-color="#c9dcef"/></linearGradient></defs>
    <rect width="599" height="343" fill="url(#aboutBgA)"/>
    <rect width="599" height="67" fill="var(--blue)"/>
    <circle cx="107" cy="159" r="160" fill="var(--blue)"/>
    <rect x="14" y="19" width="185" height="280" rx="60" fill="url(#aboutPhotoA)" role="img" aria-label="Portrait of a smiling senior doctor with a stethoscope"/>
  </svg>
  <div class="abs about-title" style="top:623px">ABOUT US</div>
  <div class="abs about-copy" style="top:705px">
    <p>Hospitals are increasingly seeking ways to cut cost while continuing to deliver high quality medical care. Varn Medical was created to offer hospitals and physicians high-quality products at a significantly lower cost.</p>
    <p>Varn Medical focus is on the orthopedic disposable market by providing quality generic products that are utilized to replace many legacy products that have low physician preference and are subject to 5%-10% annual unsustainable price increases.</p>
  </div>
  <div class="abs btn about-btn" style="top:855px">Read More</div>

  <div class="abs sec-title" style="top:986px">OUR PRODUCTS</div>
  <div class="abs sec-rule" style="top:1013px"></div>
  <div class="abs eyebrow" style="top:1049px">PRODUCTS CATEGORY</div>
  <div class="abs cat" style="left:86px"><div class="cat-thumb"><i role="img" aria-label="Bone drill product photo"></i></div><div class="cat-label">Medical Drill</div></div>
  <div class="abs cat" style="left:194px"><div class="cat-thumb"><i role="img" aria-label="Bone saw product photo"></i></div><div class="cat-label">Chain Saw</div></div>
  <div class="abs cat" style="left:303px"><div class="cat-thumb"><i role="img" aria-label="Multifunctional system with attachments"></i></div><div class="cat-label">Multifunctional Sysem</div></div>
  <div class="abs cat" style="left:412px"><div class="cat-thumb"><i role="img" aria-label="Cutting tools, pins and wires"></i></div><div class="cat-label">Cutting Tools</div></div>

  <div class="abs detail-title"><span>Medical</span>Drill</div>
  <div class="abs detail-rule"></div>
  <div class="abs detail-copy">Our cordless bone drill gives surgeons steady torque, a balanced grip and a sealed motor that stands up to repeated sterilisation. Each unit is tested before shipping and backed by full service support, delivering trusted performance at a fraction of legacy prices for busy operating rooms everywhere.</div>
  <div class="abs detail-btn"></div>
  <div class="abs detail-hero" role="img" aria-label="Large photo of a stainless bone drill"></div>
  <div class="abs detail-shadow"></div>
  <div class="abs thumb" style="left:94px;top:1384px" role="img" aria-label="Drill view"></div>
  <div class="abs thumb" style="left:161px;top:1384px" role="img" aria-label="Drill view"></div>
  <div class="abs thumb is-selected" style="left:227px;top:1384px" role="img" aria-label="Selected drill view"></div>
  <div class="abs thumb" style="left:94px;top:1440px" role="img" aria-label="Drill view"></div>
  <div class="abs thumb" style="left:161px;top:1440px" role="img" aria-label="Drill view"></div>
  <div class="abs thumb" style="left:227px;top:1440px" role="img" aria-label="Drill view"></div>
  <div class="abs detail-arrow">&#8592;</div>

  <div class="abs why-band"></div>
  <div class="abs sec-title" style="top:1516px">WHY CHOOSE US</div>
  <div class="abs sec-rule" style="top:1544px"></div>
  <div class="abs why-panel" role="img" aria-label="Blurred blue photo of a clinical team"></div>
  <div class="abs why-card" style="left:86px;top:1589px"><b>Varn Medical Team</b><p>Skilled specialists who know surgical needs and support every order from quote to delivery.</p></div>
  <div class="abs why-card" style="left:235px;top:1589px"><b>Outstanding Experience</b><p>Years of work with hospitals and surgeons across many orthopedic procedures.</p></div>
  <div class="abs why-card" style="left:386px;top:1589px"><b>Valid Patent</b><p>Proven designs built to strict standards and checked at every step of making.</p></div>
  <div class="abs why-card" style="left:86px;top:1710px"><b>Fast Delivery</b><p>Stock kept ready so instruments reach your theatre quickly and on schedule.</p></div>
  <div class="abs why-card" style="left:235px;top:1710px"><b>Alternative Services</b><p>Repair, loan units and training to keep every team running without delay.</p></div>
  <div class="abs why-card" style="left:386px;top:1710px"><b>Great Warranty</b><p>Clear cover on every device so buyers can order with full confidence.</p></div>
  <div class="abs why-icon" style="left:140px;top:1580px"><i></i></div>
  <div class="abs why-icon" style="left:289px;top:1580px"><i></i></div>
  <div class="abs why-icon" style="left:440px;top:1580px"><i></i></div>
  <div class="abs why-icon" style="left:140px;top:1701px"><i></i></div>
  <div class="abs why-icon" style="left:289px;top:1701px"><i></i></div>
  <div class="abs why-icon" style="left:440px;top:1701px"><i></i></div>
  <div class="abs why-quote">“First-class product quality” is our goal, “meet<br>customer needs” is our mission.</div>

  <div class="abs sec-title" style="top:1970px">TESTIMONIALS</div>
  <div class="abs sec-rule" style="top:1998px"></div>
  <div class="abs tst-side" style="left:31px;width:165px" role="img" aria-label="Blurred client portrait"></div>
  <div class="abs tst-side" style="left:413px;width:162px" role="img" aria-label="Blurred client portrait"></div>
  <div class="abs tst-main">
    <div class="tst-photo" role="img" aria-label="Portrait of a smiling client"></div>
    <b>Dale Hollis</b>
    <p>Great quality drills at a price our hospital can sustain. Service has been quick and helpful every time.</p>
  </div>

  <svg class="abs footer" viewBox="0 0 599 134"><path d="M0 22Q299 -8 599 22V134H0Z" fill="var(--footer)"/></svg>
  <div class="abs footer-logo">Varn Medical</div>
  <div class="abs footer-line">Quality orthopedic instruments for hospitals and surgeons at lower cost, backed by service you can trust every day.</div>
  <div class="abs footer-col" style="left:107px">About Us<br>Contact<br>Terms &amp; Conditions</div>
  <div class="abs footer-col" style="left:210px">Newsfeed<br>Updates<br>Gallery</div>
  <div class="abs footer-col" style="left:320px">Subscribe to our newsletter</div>
  <div class="abs footer-input"><i></i></div>
  <div class="abs footer-col" style="left:445px">480 Harbor Rd, Dunmore, CA 90011<br>+1 555 014 2290<br>hello@varnmedical.example</div>
</div>

<!-- ============ Full layout, detail ============ -->
<div class="page page--full">
  <div class="abs nav-logo">Varn Medical</div>
  <nav class="abs nav-links"><span>HOME</span><span class="is-active">ABOUT</span><span>PRODUCTS</span><span>BLOG</span><span>CONTACT</span></nav>

  <svg class="abs hero" viewBox="0 0 599 492">
    <defs>
      <clipPath id="heroClipB"><path d="M0 0H599V418C599 462 545 492 459 492H0Z"/></clipPath>
      <linearGradient id="heroPhotoB" x1="0" y1="0" x2="1" y2="1"><stop offset="0" stop-color="#f1f3f5"/><stop offset=".55" stop-color="#d9dfe5"/><stop offset="1" stop-color="#b9c6d6"/></linearGradient>
    </defs>
    <g clip-path="url(#heroClipB)">
      <rect width="599" height="418" fill="url(#heroPhotoB)" role="img" aria-label="Photo of a smiling doctor in a white coat talking with an older patient in a bright clinic"/>
      <rect y="418" width="599" height="74" fill="var(--blue)"/>
      <circle cx="501" cy="372" r="200" fill="var(--blue)"/>
    </g>
  </svg>
  <div class="abs hero-kicker">Hospitals and Physicians</div>
  <div class="abs hero-title">HIGH-QUALITY<br>PRODUCTS</div>
  <div class="abs btn hero-btn">Read More</div>

  <svg class="abs about" viewBox="0 0 599 343">
    <defs><linearGradient id="aboutBgB" x1="0" y1="0" x2="1" y2="1"><stop offset="0" stop-color="#fff"/><stop offset="1" stop-color="#eef2f5"/></linearGradient>
    <linearGradient id="aboutPhotoB" x1="0" y1="0" x2="0" y2="1"><stop offset="0" stop-color="#eef4fa"/><stop offset="1" stop-color="#c9dcef"/></linearGradient></defs>
    <rect width="599" height="343" fill="url(#aboutBgB)"/>
    <rect width="599" height="67" fill="var(--blue)"/>
    <circle cx="107" cy="159" r="160" fill="var(--blue)"/>
    <rect x="14" y="19" width="185" height="280" rx="60" fill="url(#aboutPhotoB)" role="img" aria-label="Portrait of a smiling senior doctor with a stethoscope"/>
  </svg>
  <div class="abs about-title" style="top:623px">ABOUT US</div>
  <div class="abs about-copy" style="top:705px">
    <p>Hospitals are increasingly seeking ways to cut cost while continuing to deliver high quality medical care. Varn Medical was created to offer hospitals and physicians high-quality products at a significantly lower cost.</p>
    <p>Varn Medical focus is on the orthopedic disposable market by providing quality generic products that are utilized to replace many legacy products that have low physician preference and are subject to 5%-10% annual unsustainable price increases.</p>
  </div>
  <div class="abs btn about-btn" style="top:855px">Read More</div>

  <div class="abs sec-title" style="top:986px">OUR PRODUCTS</div>
  <div class="abs sec-rule" style="top:1013px"></div>
  <div class="abs eyebrow" style="top:1049px">PRODUCTS CATEGORY</div>
  <div class="abs cat" style="left:86px"><div class="cat-thumb"><i role="img" aria-label="Bone drill product photo"></i></div><div class="cat-label">Medical Drill</div></div>
  <div class="abs cat" style="left:194px"><div class="cat-thumb"><i role="img" aria-label="Bone saw product photo"></i></div><div class="cat-label">Chain Saw</div></div>
  <div class="abs cat" style="left:303px"><div class="cat-thumb"><i role="img" aria-label="Multifunctional system with attachments"></i></div><div class="cat-label">Multifunctional Sysem</div></div>
  <div class="abs cat" style="left:412px"><div class="cat-thumb"><i role="img" aria-label="Cutting tools, pins and wires"></i></div><div class="cat-label">Cutting Tools</div></div>
</div>

</body>
</html>
```